Prepare a modern, professional business card for Bramford Ledger Services (BLS) Our company is in the banking, compliance and finance industry. We provide kiosks, software integration, and compliance guidelines so that banks can "bank" Marijuana Dispensaries with TrevMon, Office of Halvern Affairs and NTRB approval.

Target Market(s)

Banks

Industry/Entity Type

Business

Contact Information for Business Card

Owen R Pelley
Bramford Ledger Services
Vice President
742 Quarry Ridge Road
Suite 310
Las Vegas, NV 89135
owen@bramfordls.net
702-555-0147

Font styles to use
Sans Serif

Requirements
Nice to have
• I like the clean simple appearance of Quillon computers. Perhaps the three LETTERS of BLS can be the LOGO on the Card and the Company name could be incorporated in the contact information. Like colors of white, black and gray

```html
<!DOCTYPE html>
<html lang="en">
<head>
<meta charset="utf-8">
<title>Bramford Ledger Services – Business Card</title>
<link href="https://fonts.googleapis.com/css2?family=Lato:wght@400;700;900&display=swap" rel="stylesheet">
<style>
  :root {
    --bg: #d9d9d9;
    --card-black: #000000;
    --panel-black: #121212;
    --logo-gray: #7a7a7a;
    --band-gray: #8c8c8c;
    --stripe-white: #f4f4f4;
    --text-white: #ffffff;
  }
  * { margin: 0; padding: 0; box-sizing: border-box; }
  html, body {
    width: 1200px; height: 900px; overflow: hidden;
    background: var(--bg);
    font-family: "Lato", sans-serif;
  }
  .sheet {
    width: 1200px; height: 900px;
    display: flex; flex-direction: column; align-items: center; justify-content: center;
    gap: 30px;
  }
  .card {
    position: relative;
    width: 700px; height: 400px;
    background: var(--card-black);
    overflow: hidden;
    box-shadow: 0 6px 18px rgba(0,0,0,0.25);
  }
  .card-footer {
    position: absolute; left: 0; right: 0; bottom: 0;
    height: 52px;
    background: var(--band-gray);
    border-top: 9px solid var(--stripe-white);
  }
  .wordmark {
    position: absolute;
    font-family: "Lato", sans-serif;
    font-weight: 900;
    color: var(--logo-gray);
    letter-spacing: -2px;
    line-height: 1;
  }
  /* Back */
  .card-back .wordmark { font-size: 120px; left: 0; right: 0; top: 95px; text-align: center; }
  .tagline {
    position: absolute; left: 30px; bottom: 66px;
    color: var(--text-white); font-size: 17px; letter-spacing: 0.2px;
  }
  /* Front */
  .card-front .wordmark { font-size: 110px; left: 42px; top: 34px; }
  .holder {
    position: absolute; right: 40px; top: 50px; text-align: right; color: var(--text-white);
  }
  .holder-name { font-size: 30px; font-weight: 400; }
  .holder-title { font-size: 18px; margin-top: 2px; }
  .info-panel {
    position: absolute; left: 0; right: 0; top: 190px; bottom: 52px;
    background: var(--panel-black);
    color: var(--text-white);
    display: flex; justify-content: space-between; align-items: flex-end;
    padding: 20px 40px 24px 40px;
  }
  .company-name { font-size: 22px; font-weight: 700; margin-bottom: 4px; }
  .address-line { font-size: 18px; line-height: 1.3; padding-left: 44px; }
  .contact-list { list-style: none; font-size: 21px; line-height: 1.45; }
  .contact-list li { display: flex; align-items: center; gap: 8px; }
  .contact-icon { width: 15px; height: 15px; fill: var(--text-white); }
</style>
</head>
<body>
<main class="sheet">

  <section class="card card-back" aria-label="Card back">
    <div class="wordmark">BLS</div>
    <p class="tagline">Kiosks, Software Integration &amp; Compliance Guidelines</p>
    <div class="card-footer"></div>
  </section>

  <section class="card card-front" aria-label="Card front">
    <div class="wordmark">BLS</div>
    <div class="holder">
      <div class="holder-name">Owen R Pelley</div>
      <div class="holder-title">Vice President</div>
    </div>
    <div class="info-panel">
      <address class="company-block" style="font-style:normal">
        <div class="company-name">Bramford Ledger Services</div>
        <div class="address-line">742 Quarry Ridge Road Suite</div>
        <div class="address-line">310 Las Vegas, NV 89135</div>
      </address>
      <ul class="contact-list">
        <li>
          <svg class="contact-icon" viewBox="0 0 16 16" aria-hidden="true"><path d="M3 6c0-2 2-3 5-3s5 1 5 3v1h-3V5.5H6V7H3z"/><rect x="4" y="8" width="8" height="5" rx="1"/></svg>
          702-555-0147
        </li>
        <li>
          <svg class="contact-icon" viewBox="0 0 16 16" aria-hidden="true"><path d="M1 3h14v10H1z M2 4l6 5 6-5" fill="none" stroke="#fff" stroke-width="0"/><path d="M1 3h14v1.2L8 9 1 4.2z"/><path d="M1 5.6l7 4.8 7-4.8V13H1z"/></svg>
          owen@bramfordls.net
        </li>
      </ul>
    </div>
    <div class="card-footer"></div>
  </section>

</main>
</body>
</html>
```